Logo and label design for our product coffee scrub

We need a logo design and a packaging label design for our new brand called "Freddy Velvetoni". Best design wins 500$

It's a cosmetic brand with initial product "coffee scrub", which is a body peeling made of coffee, himalayan salt and additives. Brand will target young to middle aged women, who we will address with a very sexy and slightly provocative appeal (pictures of women wearing nothing but our coffee scrub - sample attached). Purpose of the coffee scrub is to target cellulite, stretch marks, psoriasis, varicose veins, eczema and acne.

Packaging that we will use will be a brown stand up pouch (attached) with a dimensions width 13cm, height 22cm and with a front and back sticker (dimensions width 7cm, height 14cm, round corners) or sticker that overlaps from front to back.

Looking forward on receiving your ideas!

Target Market(s)

Brand will targeting young to middle aged european women, who we will address with a very sexy and slightly provocative appeal (pictures of women wearing nothing but our coffee scrub - sample attached)

Industry/Entity Type

Product

Requirements
Must have
• Just an idea for the logo writing to use a handwriting font "Freddy Velvetoni".

For the front side of packaging label you could use a picture of a women's body wearing a coffee scrub. Label should be very sexy but not vulgar.
Nice to have
• The back side of the label should have a cheesy pick up line and declaration text (just a sample):

hi babe! so you wanna get dirty! just show me the way to your bath. but first let me give you a proper introduction of myself. my name is freddy and i'm a coffee scrub wearing nothing but 250g of finest arabic coffee and sweet orange flavour & lots of other good stuff.

by the way I will help you with cellulite, stretch marks, psoriasis, varicose veins, eczema and acne. i’ll smooth your lumps and bumps with brown sugar & sea salt, moisturise and tone your skin with cold pressed sweet almond oil, and use vitamins & minerals to work wonders from the outside in. then i’ll make us both smell good with a little orange essence.

ingredients:
Coffea Robusta Seed Powder (Coffee), Prunus Amygdalus Dulcis (Sweet Almond) Oil, Water (Aqua), Sodium Chloride (Salt), Sucrose (Brown Sugar). All ingredients organic.

net weight: 200 g

best before date:

barcode

```html
<!DOCTYPE html>
<html lang="en">
<head>
<meta charset="utf-8">
<title>Freddy Velvetoni Coffee Scrub – Label</title>
<link href="https://fonts.googleapis.com/css2?family=Gochi+Hand&family=Josefin+Sans:wght@600;700&display=swap" rel="stylesheet">
<style>
  :root {
    --ink: #111111;
    --paper: #ffffff;
    --lime: #c9d82a;
    --olive: #6b7a0e;
    --hair: #7a2a12;
    --skin: #f6cfa0;
    --skin-shade: #e9ab7c;
  }
  * { margin: 0; padding: 0; box-sizing: border-box; }
  html, body {
    width: 927px;
    height: 1200px;
    overflow: hidden;
    background: var(--paper);
  }
  .canvas {
    position: relative;
    width: 927px;
    height: 1200px;
    font-family: "Josefin Sans", sans-serif;
    color: var(--ink);
  }
  .label-art {
    position: absolute;
    inset: 0;
    width: 927px;
    height: 1200px;
  }
  .brand-name {
    position: absolute;
    left: 484px;
    top: 152px;
    font-family: "Gochi Hand", cursive;
    font-weight: 400;
    font-size: 60px;
    line-height: 74px;
    color: var(--ink);
    white-space: nowrap;
  }
  .brand-name span { display: block; }
  .brand-name .second { margin-left: 14px; }
  .product-type {
    position: absolute;
    left: 490px;
    top: 336px;
    font-size: 23px;
    font-weight: 700;
    letter-spacing: 5px;
  }
  .pickup-line {
    position: absolute;
    left: 428px;
    top: 452px;
    font-size: 20px;
    font-weight: 700;
    line-height: 31.5px;
    white-space: nowrap;
  }
  .pickup-line span { display: block; }
  .pickup-line .in-1 { padding-left: 14px; }
  .pickup-line .in-2 { padding-left: 20px; }
  .pickup-line .in-3 { padding-left: 23px; }
  .declaration {
    position: absolute;
    right: 175px;
    top: 868px;
    text-align: right;
    font-weight: 700;
    text-transform: uppercase;
  }
  .ingredients {
    font-size: 11.5px;
    line-height: 12.8px;
  }
  .net-weight, .best-before {
    font-size: 14.5px;
    margin-top: 20px;
  }
  .best-before { margin-top: 22px; }
</style>
</head>
<body>
<div class="canvas">
  <svg class="label-art" viewBox="0 0 600 776.7" xmlns="http://www.w3.org/2000/svg">
    <defs>
      <clipPath id="label-shape">
        <rect x="142" y="78" width="368" height="619" rx="10" ry="10"/>
      </clipPath>
      <linearGradient id="band-fade" x1="0" y1="0" x2="1" y2="0">
        <stop offset="0.45" stop-color="var(--lime)"/>
        <stop offset="1" stop-color="var(--olive)"/>
      </linearGradient>
      <linearGradient id="figure-tone" x1="0" y1="0" x2="0" y2="1">
        <stop offset="0" stop-color="var(--hair)"/>
        <stop offset="0.2" stop-color="var(--skin)"/>
        <stop offset="1" stop-color="var(--skin-shade)"/>
      </linearGradient>
    </defs>
    <rect class="label-bg" x="142" y="78" width="368" height="619" rx="10" ry="10" fill="var(--paper)"/>
    <g clip-path="url(#label-shape)">
      <polygon class="accent-strip" points="290,258 510,200 510,222 290,276" fill="url(#band-fade)"/>
      <polygon class="main-band" points="140,298 510,240 510,480 140,560" fill="url(#band-fade)"/>
      <rect class="pinup-area" role="img" aria-label="Illustration of a red-haired pin-up woman in black underwear leaning against the band"
            x="142" y="78" width="130" height="619" fill="url(#figure-tone)"/>
    </g>
    <rect class="label-edge" x="142" y="78" width="368" height="619" rx="10" ry="10" fill="none" stroke="var(--ink)" stroke-width="1.8"/>
  </svg>

  <h1 class="brand-name"><span>Freddy</span><span class="second">Velvetoni</span></h1>
  <p class="product-type">COFFEE SCRUB</p>

  <p class="pickup-line">
    <span>Hi babe! so you wanna get dirty!</span>
    <span>just show me the way to your</span>
    <span>bath. but first let me give you</span>
    <span>a proper introduction of myself.</span>
    <span>My name is freddy and I'm a</span>
    <span>coffee scrub wearing nothing</span>
    <span class="in-1">but 250g of finest arabic coffee</span>
    <span class="in-2">and sweet orange flavour &amp;</span>
    <span class="in-3">lots of other good stuff.</span>
  </p>

  <div class="declaration">
    <p class="ingredients">
      Ingredients:<br>
      Coffea Robusta Seed Powder (Coffee),<br>
      Prunus Amygdalus Dulcis (Sweet Almond)<br>
      Oil, Water (Aqua), Sodium Chloride (Salt),<br>
      Sucrose (Brown Sugar).<br>
      All ingredients organic.
    </p>
    <p class="net-weight">Net weight: 200 g</p>
    <p class="best-before">Best before date:</p>
  </div>
</div>
</body>
</html>
```